Verpackungsdesign für Kaffeerösterei
Zielgruppe
wir Rösten Kaffee. Wir haben uns darauf Spezialisiert Hochwertigen Premium Caffe Crema herzustellen und bieten auch nur diesen in Unserem Shop www.brunor7-kaffee.de an. wir bieten 250gr. 500gr. Kaffee an. .
Es kann gerne verrückt oder anders sein, dennoch aber sehr edel.
die Zielgruppe ist weitgestreut, aber laut unserern Daten ist die Ideale Zielgruppe der 52 Jährige Mann, der Wert auf Hochwertige Genussmittel legt und auch bereit ist mehr Geld dafür zu bezahlen.
ich habe bereits ein beispiel design und die Druckvorlage bereitgestellt.
Aufgabenstellung
das Konzept unserer Internetseite sollte berücksichtigt werden, ansonsten ist dem Kreativen kopf keine Grenzen gesetzt.

```html
<!DOCTYPE html>
<html lang="de">
<head>
<meta charset="utf-8">
<title>Brunor 7 – Cafe Crema 500g</title>
<link href="https://fonts.googleapis.com/css2?family=Anton&family=Oswald:wght@300;400&display=swap" rel="stylesheet">
<style>
  :root {
    --stage: #9c9c9c;
    --cream: #ede5e2;
    --rose: #d5bcb3;
    --rust: #8a3f22;
    --pine: #0b302d;
    --amber: #b8713e;
    --ink: #030303;
    --logo-grey: #a9b3b3;
    --title: #dcdcdc;
    --copy: #e6e6e6;
    --seal: #b08a2a;
    --seal-ring: #1a1408;
  }
  * { margin: 0; padding: 0; box-sizing: border-box; }
  html, body {
    width: 791px; height: 1200px; overflow: hidden;
    background: var(--stage);
  }
  .canvas { position: relative; width: 791px; height: 1200px; }
  .pack-front {
    position: absolute; left: 116px; top: 134px;
    width: 538px; height: 1046px; overflow: hidden;
    background: var(--ink);
  }
  .pack-artwork {
    position: absolute; left: 0; top: 0; width: 100%; height: 817px;
    background: linear-gradient(155deg,
      var(--cream) 0%, var(--rose) 22%, var(--rust) 42%,
      var(--pine) 62%, var(--amber) 82%, var(--amber) 100%);
  }
  .pack-artwork::after {
    content: ""; position: absolute; left: 0; right: 0; bottom: 0; height: 110px;
    background: linear-gradient(to bottom, rgba(3,3,3,0), var(--ink));
  }
  .brand-name {
    position: absolute; left: 0; width: 100%; top: 652px;
    text-align: center;
    font-family: "Anton", sans-serif; font-size: 32px; letter-spacing: 3px;
    color: var(--logo-grey);
  }
  .quality-seal {
    position: absolute; left: 331px; top: 712px;
    width: 100px; height: 100px; border-radius: 50%;
    background: var(--seal); border: 6px solid var(--seal-ring);
  }
  .product-title {
    position: absolute; left: 0; width: 100%; top: 752px;
    text-align: center;
    font-family: "Anton", sans-serif; font-weight: 400; font-size: 50px; line-height: 44px;
    color: var(--title); letter-spacing: 1px;
  }
  .taste-notes {
    position: absolute; left: 0; width: 100%; top: 855px;
    text-align: center;
    font-family: "Oswald", sans-serif; font-weight: 300; font-size: 16px; line-height: 20px;
    color: var(--copy);
  }
  .net-weight {
    position: absolute; left: 0; width: 100%; top: 990px;
    text-align: center;
    font-family: "Oswald", sans-serif; font-weight: 400; font-size: 21px;
    color: var(--copy);
  }
</style>
</head>
<body>
<main class="canvas">
  <section class="pack-front">
    <div class="pack-artwork" role="img" aria-label="Abstrakte Grafik aus geschwungenen Flächen in Creme, Rosé, Rostbraun, Tannengrün und Bernstein"></div>
    <p class="brand-name">BRUNOR 7</p>
    <div class="quality-seal"></div>
    <h1 class="product-title">CAFE<br>CREMA</h1>
    <p class="taste-notes">Geschmacksnote:Dunkle<br>Schokolade, karam</p>
    <p class="net-weight">Net wt. 500g</p>
  </section>
</main>
</body>
</html>
```